Web Design for Harbor vNet

Need a website for 24/7 online Tv station. Looking for something unique, fresh and different.

When you click on site, I want viewers to automatically see video player. Video player should take up about 70% screen. Still need sections to show thumbnail clicks of our mission - Inspire, Inform and Entertain. Also need section to highlight new shows or events.

This is a family based TV station that will feature Christian content, news, per pay view movies, music videos, sermons from churches. I want site to appeal to 18 -40 year demo graphic. Even though based in California, I also want site appealing enough to all cultures worldwide.

Go to Streamly and search our channel (harborvnet) for some footages and logo.

Also visit www.harborvnet-demo.com to see logo. Need a design that matches logo.

Updates as of 8/28/13:-

http://video.kindhandsaid-demo.org/channel/animals-agriculture/
KHTV – like the look and feel. Left side to have 16:9 screen with player and on the right will be still pictures slide show

http://www.zuvwatch-demo.com/?camp=XoX512&tracking_ID=000000&K_CLICKID=00000000-0000-0000-0000-000000000000#home/
ZUV – I like the 16:9 screen (I don’t want mine too big – about 60% of screen)
I want a black background that will also match Harbor vNet red and white logo (see uploaded file)
Updates

KHTV – like the look and feel.  Left side to have 16:9 screen with player and on the right will be still pictures slide show

 

Reason: Need more time for poll results to come in and narrow down to one or two designs.

Target Market(s)

zPhone, zTab generation

I like the look and feel Kind Hands Aid TV

Industry/Entity Type

Tv

```html
<!DOCTYPE html>
<html lang="en">
<head>
<meta charset="utf-8">
<title>Harbor vNet</title>
<link rel="stylesheet" href="https://fonts.googleapis.com/css2?family=Questrial&family=Arimo:wght@400;700&display=swap">
<style>
  :root {
    --page-bg: #ffffff;
    --bar-top: #3a3a3a;
    --bar-bottom: #161616;
    --black: #000000;
    --panel: #111111;
    --panel-edge: #1e1e1e;
    --red: #e8141f;
    --red-edge: #9c0e14;
    --white: #ffffff;
    --muted: #8a8a8a;
    --text-dim: #b9b9b9;
    --frame: #050505;
  }
  * { box-sizing: border-box; margin: 0; padding: 0; }
  html, body { width: 1200px; height: 1000px; overflow: hidden; background: var(--page-bg); }
  body { position: relative; font-family: "Arimo", Arial, sans-serif; }
  .site { position: absolute; left: 53px; top: 0; width: 1097px; height: 1000px; background: var(--black); }
  .abs { position: absolute; }

  /* top utility bar */
  .utility-bar { left: 0; top: 0; width: 1097px; height: 30px; background: linear-gradient(var(--bar-top), var(--bar-bottom)); }
  .utility-bar .login { left: 664px; top: 9px; font-size: 9px; color: var(--muted); padding-right: 8px; border-right: 1px solid #555; }
  .search { left: 698px; top: 3px; width: 202px; height: 22px; border-radius: 8px; background: #2a2a2a; box-shadow: inset 0 1px 3px #000; }
  .search span { position: absolute; left: 10px; top: 6px; font-size: 8px; color: var(--text-dim); }
  .search svg { position: absolute; right: 8px; top: 3px; }

  /* header */
  .header { left: 0; top: 30px; width: 1097px; height: 98px; background: var(--black); border-bottom: 1px solid var(--panel-edge); }
  .brand { font-family: "Questrial", sans-serif; color: var(--white); white-space: nowrap; }
  .header .brand { left: 214px; top: 28px; font-size: 28px; }
  .nav { right: 199px; top: 47px; display: flex; gap: 11px; font-size: 8.5px; font-weight: 700; color: #e6e6e6; white-space: nowrap; }

  /* hero */
  .hero { left: 0; top: 128px; width: 1097px; height: 310px; background: var(--panel); }
  .player { left: 214px; top: 9px; width: 479px; height: 289px; background: var(--black); border-radius: 6px; border: 1px solid #222; overflow: hidden; }
  .player .frame-photo { left: 79px; top: 4px; width: 307px; height: 277px; background: radial-gradient(ellipse at 60% 35%, #3f8a3a 0%, #1c4a1e 45%, #0b160b 100%); }
  .player .title { left: 12px; top: 21px; font-family: "Questrial", sans-serif; font-size: 13px; color: #9a9a9a; }
  .player .subtitle { left: 12px; top: 36px; font-size: 8px; color: #8a8a8a; }
  .player .big-play { left: 164px; top: 93px; }
  .player .controls { left: 12px; top: 262px; }
  .player .controls-right { right: 12px; top: 262px; }
  .pillar { left: 700px; width: 198px; height: 90px; background: var(--black); border-radius: 5px; border: 1px solid #222; }
  .pillar .thumb { left: 4px; top: 4px; width: 189px; height: 81px; background: linear-gradient(90deg, #6d6a5f 0%, #8d8577 40%, #7a2a26 41%, #9a3a34 70%, #7b6a5a 100%); }
  .pillar .label { left: 11px; top: 40px; font-family: "Questrial", sans-serif; font-size: 12px; color: var(--white); letter-spacing: 0.3px; }

  /* feature bands */
  .band { left: 0; width: 1097px; }
  .band.shows { top: 438px; height: 213px; background: var(--red); border-top: 2px solid var(--red-edge); border-bottom: 2px solid #3a0a0c; }
  .band.events { top: 651px; height: 227px; background: var(--panel); border-bottom: 1px solid var(--panel-edge); }
  .band h2 { position: absolute; left: 214px; font-family: "Questrial", sans-serif; font-weight: 400; font-size: 17px; color: var(--white); }
  .band h3 { position: absolute; left: 214px; font-family: "Questrial", sans-serif; font-weight: 400; font-size: 13px; }
  .band p { position: absolute; left: 215px; width: 215px; font-size: 9.4px; line-height: 11.5px; }
  .band .more { position: absolute; left: 214px; font-size: 9px; }
  .shows h2 { top: 16px; } .shows h3 { top: 44px; color: var(--black); }
  .shows p { top: 76px; color: var(--black); } .shows .more { top: 159px; color: var(--black); }
  .events h2 { top: 26px; } .events h3 { top: 57px; color: #a9a9a9; }
  .events p { top: 90px; color: #b0b0b0; } .events .more { top: 174px; color: #c9c9c9; }
  .media { width: 227px; height: 131px; background: var(--frame); border: 1px solid #777; }
  .events .media { border-color: #2a2a2a; }
  .media .fill { position: absolute; left: 4px; top: 4px; width: 217px; height: 121px; }
  .shows .fill { background: linear-gradient(90deg, #d9b98a 0%, #c9a27c 35%, #8a6c8c 60%, #3c62a3 100%); }
  .events .fill { background: linear-gradient(90deg, #e6c48a 0%, #c99a6a 45%, #5d7f3f 70%, #3c5a2a 100%); }
  .media .tag { position: absolute; left: 9px; bottom: 12px; font-size: 9px; color: #6a6a6a; }

  /* footer */
  .footer { left: 0; top: 878px; width: 1097px; height: 122px; background: var(--black); }
  .footer .brand { left: 218px; top: 58px; font-size: 18px; }
  .footer .divider { left: 350px; top: 35px; width: 1px; height: 87px; background: #222; }
  .footer .legal { left: 372px; top: 64px; font-size: 7px; line-height: 9px; color: #666; }
  .follow { left: 700px; top: 50px; font-family: "Questrial", sans-serif; font-size: 10px; color: #777; text-decoration: underline; }
  .social { left: 700px; top: 75px; display: flex; gap: 5px; }
  .social span { width: 22px; height: 22px; background: var(--white); border-radius: 3px; }
</style>
</head>
<body>
<div class="site">
  <div class="abs utility-bar">
    <span class="abs login">Login</span>
    <div class="abs search"><span>Search</span>
      <svg width="16" height="16" viewBox="0 0 16 16"><circle cx="6.5" cy="6.5" r="4.5" fill="none" stroke="#aaa" stroke-width="2"/><line x1="10" y1="10" x2="14" y2="14" stroke="#aaa" stroke-width="2.5"/></svg>
    </div>
  </div>

  <header class="abs header">
    <div class="abs brand">Harbor vNet</div>
    <nav class="abs nav"><span>HOME</span><span>PROGRAMS</span><span>ADVERTISE</span><span>ABOUT US</span><span>SUBSCRIBE</span><span>OPPORTUNITIES</span><span>CONTACT US</span></nav>
  </header>

  <section class="abs hero">
    <div class="abs player">
      <div class="abs frame-photo" role="img" aria-label="Video still of a singer performing with a microphone on a green-lit stage"></div>
      <div class="abs title">Title of the Video</div>
      <div class="abs subtitle">Sub Title goes Here</div>
      <svg class="abs big-play" width="100" height="100" viewBox="0 0 100 100">
        <circle cx="50" cy="50" r="46" fill="rgba(255,255,255,0.12)" stroke="rgba(220,220,220,0.8)" stroke-width="4"/>
        <path d="M38 26 L74 50 L38 74 Z" fill="rgba(235,235,235,0.75)"/>
      </svg>
      <svg class="abs controls" width="60" height="20" viewBox="0 0 60 20">
        <circle cx="10" cy="10" r="9" fill="#555" stroke="#999" stroke-width="1.5"/><path d="M7 5 L15 10 L7 15 Z" fill="#ddd"/>
        <path d="M34 7 h4 l5 -4 v14 l-5 -4 h-4 Z" fill="#ccc"/>
        <path d="M46 6 q3 4 0 8 M49 4 q5 6 0 12" stroke="#ccc" stroke-width="1.5" fill="none"/>
      </svg>
      <svg class="abs controls-right" width="50" height="20" viewBox="0 0 50 20">
        <circle cx="9" cy="10" r="8" fill="#777"/><rect x="8" y="8" width="2" height="7" fill="#222"/><circle cx="9" cy="5.5" r="1.2" fill="#222"/>
        <circle cx="44" cy="3" r="2.8" fill="#ccc"/><circle cx="34" cy="10" r="2.8" fill="#ccc"/><circle cx="44" cy="17" r="2.8" fill="#ccc"/>
        <path d="M44 3 L34 10 L44 17" stroke="#ccc" stroke-width="1.5" fill="none"/>
      </svg>
    </div>
    <a class="abs pillar" style="top:9px"><div class="abs thumb" role="img" aria-label="Coffee cup beside an open book and pen"></div><span class="abs label">INSPIRE</span></a>
    <a class="abs pillar" style="top:109px"><div class="abs thumb" role="img" aria-label="Coffee cup beside an open book and pen"></div><span class="abs label">INFORM</span></a>
    <a class="abs pillar" style="top:208px"><div class="abs thumb" role="img" aria-label="Coffee cup beside an open book and pen"></div><span class="abs label">ENTERTAIN</span></a>
  </section>

  <section class="abs band shows">
    <h2>New Shows</h2>
    <h3>Lorem Ipsum</h3>
    <p>Lorem Ipsum is simply dummy text of the printing and typesetting industry. Lorem Ipsum has been the industry's standard dummy text ever since</p>
    <span class="more">+ view more</span>
    <div class="abs media" style="left:444px;top:45px"><div class="fill" role="img" aria-label="Group of smiling young friends"></div><span class="tag">demo image</span></div>
    <div class="abs media" style="left:674px;top:45px"><div class="fill" role="img" aria-label="Group of smiling young friends"></div><span class="tag">demo image</span></div>
  </section>

  <section class="abs band events">
    <h2>Events</h2>
    <h3>Lorem Ipsum</h3>
    <p>Lorem Ipsum is simply dummy text of the printing and typesetting industry. Lorem Ipsum has been the industry's standard dummy text ever since</p>
    <span class="more">+ view more</span>
    <div class="abs media" style="left:444px;top:58px"><div class="fill" role="img" aria-label="Couple outdoors with a red rose"></div><span class="tag" style="bottom:40px">demo image</span></div>
    <div class="abs media" style="left:674px;top:58px"><div class="fill" role="img" aria-label="Couple outdoors with a red rose"></div><span class="tag" style="bottom:32px">demo image</span></div>
  </section>

  <footer class="abs footer">
    <div class="abs brand">Harbor vNet</div>
    <div class="abs divider"></div>
    <div class="abs legal">2013. All Right Reserved Harbor vNet</div>
    <div class="abs follow">FOLLOW US</div>
    <div class="abs social"><span></span><span></span><span></span></div>
  </footer>
</div>
</body>
</html>
```